依頼詳細
【サイトの最大の要望】
・新規集客(ネット予約がゴール)
・院の認知アップ(新規開業のため)

【強み】
・お待たせしないシステム
・保険適用の漢方治療

【ターゲット】
・世代:30代以降
・性別:やや女性寄り

【完成イメージ】
全面は白で、植物などの緑、茶色・木目調を差し色にしています。
待合室については濃いめの木目調のカウンターテーブルがあり、
ペンダントライトでカフェ風な作りになっています。

・完成イメージ
http://vrview.mokunoie-kenchiku.jp/wt_movie/p_mv/48391qzpa7r/vtour/tour.html

・木乃家建築で内観がイメージに近い事例
http://www.mokunoie-kenchiku.jp/medical/doctor/example/morita_naika.html

【参考サイト】
https://www.kawabe-dining.jp/lavendora/
https://sorine-cafe.jp/
http://www.kirigaoka-tei.com/restaurant/wrencafe/
http://waffle.tovari-works.jp/
http://www.almondlodge.jp/#!page4

【サイトマップ】
1.TOP
2.初めての方へ
3.医院について
4.当院の特徴
5.院長紹介
6.よくある質問
7.ブログ(一覧)
∟8.ブログ(詳細)
9.お知らせ(一覧)
∟10.お知らせ(詳細)
11.耳の病気
12.鼻の病気
13.口・のどの病気
14.頭・顔・首の病気
15.風邪の症状
16.更年期の症状にお悩みの方
17.冷えにお悩みの方へ
18.不眠にお悩みの方へ
19.めまい・耳鳴りにお悩みの方へ
20.体質改善
希望イメージ
• シンプル
複雑
• 単色
カラフル
• 暗い
明るい
• 日常
高級
• 遊び心
厳粛
• 未来的
伝統的
• 女性的
男性的
希望する色
ベースは白。植物などの緑、木目調の濃い茶色を差し色
納品ファイル
• フォトショップ形式 (.psd)
• PNG形式 (.png)
補足説明
【店舗へのご連絡はおやめください】
ワークミツ規約にもありますが、店舗への通常業務に支障が出るため、
直接電話等のお問い合わせをお控え頂きますよう、ご協力願います。

【素材写真】
素材については、ピクセラのカンプ画像をご使用ください。
選定後に正規データをお渡し致します。
(画像はマンスリーパック内でお願い致します。)
依頼公開後の追記内容
ワイヤフレームを添付致します。
提案期間を延長致します。
提案数がないため、期限を延長致します。
こちら提案数が欲しいため、延長致します。
■ 選んだ理由

一見してシンプルながら目を引くデザインで、院のイメージに合っていたため

■ 提案者全員のお礼・コメント

この度はご提案くださり、ありがとうございました。
また機会がございましたら、どうぞ宜しくお願い致します。

```html
<!DOCTYPE html>
<html lang="ja">
<head>
<meta charset="utf-8">
<title>すずらん耳鼻咽喉科</title>
<link href="https://fonts.googleapis.com/css2?family=Noto+Sans+JP:wght@300;400;500;700&family=Quicksand:wght@500;700&display=swap" rel="stylesheet">
<style>
:root{
  --green:#8fb83a;
  --green-soft:#eef4e0;
  --brown:#5a4a3f;
  --brown-dark:#4a3c33;
  --text:#4b4038;
  --muted:#8a7f77;
  --line:#e4ded8;
  --bg:#ffffff;
  --bg-soft:#f6f4f1;
}
*{box-sizing:border-box;margin:0;padding:0}
html,body{width:1200px;height:3488px;overflow:hidden}
body{font-family:"Noto Sans JP",sans-serif;color:var(--text);background:var(--bg);font-size:13px;position:relative}
.en{font-family:"Quicksand",sans-serif}
.abs{position:absolute}
.img{display:block}
/* hero */
.hero{position:absolute;left:0;top:0;width:1200px;height:500px;background:linear-gradient(180deg,#d6e6f2 0%,#eef3f6 45%,#e8e4de 70%,#cfc6bb 100%)}
.logo{position:absolute;left:40px;top:40px;display:flex;align-items:center;gap:10px;font-size:24px;font-weight:500;color:var(--brown)}
.logo i{width:16px;height:16px;border-radius:50%;background:var(--green)}
.contact{position:absolute;left:488px;top:22px;width:560px;height:118px;background:rgba(255,255,255,.92);display:flex;padding:14px 18px;gap:18px}
.contact .addr{font-size:11px;color:var(--muted)}
.tel{font-family:"Quicksand",sans-serif;font-weight:700;color:var(--green);font-size:30px;line-height:1.2}
.tel small{font-size:16px;margin-right:4px}
.btn-reserve{display:inline-block;background:var(--brown);color:#fff;font-size:12px;border-radius:20px;padding:5px 22px;margin-top:4px}
.hours{border-collapse:collapse;font-size:10px;color:var(--text)}
.hours th,.hours td{border-bottom:1px solid var(--line);padding:6px 5px;text-align:center;font-weight:400}
.hours th{color:var(--muted)}
.hours td.o{color:var(--green)}
/* nav */
.gnav{position:absolute;left:0;top:500px;width:1200px;height:60px;background:#fff;border-bottom:1px solid var(--line);display:flex;justify-content:center}
.gnav a{width:130px;display:flex;align-items:center;justify-content:center;font-size:13px;color:var(--text);text-decoration:none;border-left:1px solid var(--line)}
.gnav a:last-child{border-right:1px solid var(--line)}
.side-tab{position:absolute;right:0;top:630px;width:36px;height:170px;background:var(--brown);color:#fff;writing-mode:vertical-rl;font-size:12px;display:flex;align-items:center;justify-content:center;border-radius:6px 0 0 6px;letter-spacing:2px}
/* services */
.services{position:absolute;left:0;top:560px;width:1200px;height:690px;background:var(--bg-soft)}
.svc{position:absolute;top:50px;width:440px}
.svc-head{text-align:center;margin-bottom:22px}
.svc-icon{width:56px;height:56px;border-radius:50%;background:var(--green);margin:0 auto 10px;display:flex;align-items:center;justify-content:center}
.svc-head h2{font-size:20px;font-weight:500;color:var(--brown)}
.svc-photo{height:200px;position:relative}
.svc-photo .label{position:absolute;left:16px;bottom:16px;background:rgba(255,255,255,.92);padding:10px 16px;font-size:14px}
.svc-grid{display:grid;grid-template-columns:1fr 1fr;gap:8px;margin-top:8px}
.svc-item{background:#fff;height:88px;display:flex;align-items:center;gap:12px;padding:8px}
.svc-item .img{width:72px;height:72px}
.svc-item span{font-size:13px;flex:1}
.svc-item b{color:var(--green);font-weight:400}
/* features */
.section-title{text-align:center;font-size:22px;font-weight:500;color:var(--brown)}
.section-title:before{content:"";display:block;width:8px;height:8px;border-radius:50%;background:var(--green);margin:0 auto 10px}
.features{position:absolute;left:0;top:1250px;width:1200px;height:530px}
.feat{position:absolute;top:110px;width:260px;text-align:center}
.feat .num{position:absolute;left:0;top:-10px;font-family:"Quicksand",sans-serif;font-size:40px;color:var(--green);font-weight:500}
.feat .circle{width:170px;height:170px;border-radius:50%;margin:0 auto}
.feat h3{font-size:15px;font-weight:500;margin:20px 0 10px;border-bottom:1px solid var(--line);padding-bottom:10px}
.feat p{font-size:11px;line-height:1.9;color:var(--muted);text-align:left}
.btn-more{position:absolute;left:50%;transform:translateX(-50%);width:170px;height:34px;border-radius:17px;background:var(--brown);color:#fff;font-size:12px;display:flex;align-items:center;justify-content:center}
/* director */
.director{position:absolute;left:0;top:1780px;width:1200px;height:530px;background:linear-gradient(135deg,#d9d4cf,#b9b1a9 60%,#e8e4df)}
.dir-card{position:absolute;left:240px;top:50px;width:720px;height:430px;background:rgba(255,255,255,.95);padding:40px 50px}
.dir-name{font-size:16px;margin:30px 0 14px}
.dir-name small{color:var(--green);font-size:11px;margin-left:10px}
.dir-text{width:380px;font-size:11px;line-height:2;color:var(--muted)}
.dir-photo{position:absolute;right:60px;top:120px;width:190px;height:190px;border-radius:50%}
/* news blog */
.info{position:absolute;left:0;top:2330px;width:1200px;height:480px}
.col{position:absolute;top:30px;width:430px}
.col h2{text-align:center;font-size:18px;font-weight:500;color:var(--brown);margin-bottom:26px}
.news li{list-style:none;display:flex;gap:22px;font-size:11px;padding:12px 0;border-bottom:1px dashed var(--line)}
.news time{color:var(--muted)}
.divider{position:absolute;left:599px;top:40px;width:1px;height:400px;background:var(--line)}
.blog-item{display:flex;gap:14px;margin-bottom:22px}
.blog-item .img{width:90px;height:90px}
.tag{display:inline-block;background:var(--green);color:#fff;font-size:10px;padding:2px 8px}
.blog-item p{font-size:12px;margin:6px 0;line-height:1.6}
.blog-item small{font-size:10px;color:var(--muted);line-height:1.6;display:block}
/* map */
.map{position:absolute;left:0;top:2820px;width:1200px;height:300px;background:linear-gradient(135deg,#eceae4,#e2e6dc 50%,#ecebe6)}
/* footer */
.footer{position:absolute;left:0;top:3120px;width:1200px;height:368px;background:var(--brown);color:#efe9e3}
.to-top{position:absolute;left:570px;top:-22px;width:60px;height:30px;background:var(--brown);border-radius:30px 30px 0 0;display:flex;align-items:center;justify-content:center}
.f-logo{font-size:22px;font-weight:500;display:flex;align-items:center;gap:10px}
.f-logo i{width:14px;height:14px;border-radius:50%;background:var(--green)}
.footer .tel{color:#fff;font-size:40px}
.footer .hours th,.footer .hours td{border-color:#7a6a5e;color:#efe9e3;padding:7px 8px}
.footer .hours td.o{color:#c5dd86}
.f-nav{position:absolute;top:50px;display:flex;flex-direction:column;gap:12px;font-size:11px}
.f-nav h4{font-size:12px;font-weight:500;color:#c5dd86;margin-bottom:2px}
.copy{position:absolute;right:150px;bottom:18px;font-size:10px;color:#b3a597}
</style>
</head>
<body>

<header class="hero" role="img" aria-label="白い外壁の医院外観写真と青空">
  <div class="logo"><i></i>すずらん耳鼻咽喉科</div>
  <div class="contact">
    <div>
      <div class="addr">〒310-0099 茨城県水戸市みどり町1-2-3</div>
      <div class="tel"><small>tel.</small>029-555-0184</div>
      <span class="btn-reserve">ネット予約はこちらから ›</span>
    </div>
    <table class="hours">
      <tr><th>診療時間</th><th>月</th><th>火</th><th>水</th><th>木</th><th>金</th><th>土</th><th>日</th></tr>
      <tr><td>9:00 - 12:30</td><td class="o">●</td><td class="o">●</td><td class="o">●</td><td>／</td><td class="o">●</td><td class="o">●</td><td>／</td></tr>
      <tr><td>15:00 - 18:30</td><td class="o">●</td><td class="o">●</td><td class="o">●</td><td>／</td><td class="o">●</td><td>／</td><td>／</td></tr>
    </table>
  </div>
</header>

<nav class="gnav">
  <a>初めての方へ</a><a>医院について</a><a>当院の特徴</a><a>院長紹介</a><a>耳鼻咽喉科診療</a><a>漢方治療</a><a>よくある質問</a>
</nav>
<div class="side-tab">ネット予約はこちら</div>

<section class="services">
  <div class="svc" style="left:150px">
    <div class="svc-head">
      <div class="svc-icon"><svg width="26" height="26" viewBox="0 0 26 26"><path d="M9 20c0-5 8-5 8-11a5 5 0 0 0-10 0" fill="none" stroke="#fff" stroke-width="2.2" stroke-linecap="round"/></svg></div>
      <h2>耳鼻咽喉科</h2>
    </div>
    <div class="svc-photo img" role="img" aria-label="耳に手を当てる女性の写真" style="background:linear-gradient(120deg,#e6dfd6,#d7e4ee)"><div class="label">耳の病気 ›</div></div>
    <div class="svc-grid">
      <div class="svc-item"><div class="img" role="img" aria-label="鼻を押さえる人の写真" style="background:#e9dfd5"></div><span>鼻の病気</span><b>›</b></div>
      <div class="svc-item"><div class="img" role="img" aria-label="のどを押さえる人の写真" style="background:#e3ddd4"></div><span>口・のどの病気</span><b>›</b></div>
      <div class="svc-item"><div class="img" role="img" aria-label="頭痛に悩む人の写真" style="background:#ece4da"></div><span>頭・顔・首の病気</span><b>›</b></div>
      <div class="svc-item"><div class="img" role="img" aria-label="風邪をひいた人の写真" style="background:#dfe5e8"></div><span>風邪の症状</span><b>›</b></div>
    </div>
  </div>
  <div class="svc" style="left:610px">
    <div class="svc-head">
      <div class="svc-icon"><svg width="26" height="26" viewBox="0 0 26 26"><path d="M5 21C5 10 12 5 21 5c0 9-5 16-16 16zM5 21l9-9" fill="none" stroke="#fff" stroke-width="2.2" stroke-linecap="round"/></svg></div>
      <h2>漢方治療</h2>
    </div>
    <div class="svc-photo img" role="img" aria-label="ソファでくつろぐ女性の写真" style="background:linear-gradient(120deg,#efe9df,#dfe6d3)"><div class="label">更年期の症状にお悩みの方へ ›</div></div>
    <div class="svc-grid">
      <div class="svc-item"><div class="img" role="img" aria-label="体を温める女性の写真" style="background:#ebe1d6"></div><span>冷えにお悩みの方へ</span><b>›</b></div>
      <div class="svc-item"><div class="img" role="img" aria-label="ベッドで休む女性の写真" style="background:#e4e1da"></div><span>不眠にお悩みの方へ</span><b>›</b></div>
      <div class="svc-item"><div class="img" role="img" aria-label="こめかみを押さえる女性の写真" style="background:#e8e2d8"></div><span>めまい・耳鳴りにお悩みの方へ</span><b>›</b></div>
      <div class="svc-item"><div class="img" role="img" aria-label="ヨガをする女性の写真" style="background:#e2e8da"></div><span>体質改善</span><b>›</b></div>
    </div>
  </div>
</section>

<section class="features">
  <h2 class="section-title" style="margin-top:40px">当院の特徴</h2>
  <div class="feat" style="left:150px"><span class="num">01</span>
    <div class="circle" role="img" aria-label="スマートフォンを持つ女性の写真" style="background:linear-gradient(135deg,#eee7dc,#d9e3ea)"></div>
    <h3>ネットでらくらく予約</h3>
    <p>スマートフォンやパソコンから24時間いつでも予約できます。院内での待ち時間を減らし、ご来院いただけます。</p></div>
  <div class="feat" style="left:470px"><span class="num">02</span>
    <div class="circle" role="img" aria-label="生薬が並ぶ写真" style="background:linear-gradient(135deg,#c9a57a,#8a6a48)"></div>
    <h3>保険適用の漢方治療</h3>
    <p>体質に合わせた漢方薬を保険診療の範囲でご提案します。不調の根本から、やさしく整えていきます。</p></div>
  <div class="feat" style="left:790px"><span class="num">03</span>
    <div class="circle" role="img" aria-label="観葉植物のある院内の写真" style="background:linear-gradient(135deg,#dfe6d0,#a9b98a)"></div>
    <h3>お薬の相談が入ります</h3>
    <p>ご不明な点はお気軽にご相談ください。お薬の飲み方や組み合わせについても丁寧にご説明いたします。</p></div>
  <div class="btn-more" style="top:466px">詳しくはこちら ›</div>
</section>

<section class="director" role="img" aria-label="カフェ風の待合室の写真">
  <div class="dir-card">
    <h2 class="section-title">院長紹介</h2>
    <div class="dir-name">川村 誠<small>DIRECTOR</small></div>
    <p class="dir-text">このたび地域の皆さまのかかりつけ医として開院いたしました。耳や鼻、のどの不調はもちろん、漢方を取り入れた治療で体全体の健康をサポートいたします。お気軽にご来院ください。<br><br>患者さま一人ひとりのお話をしっかり伺い、安心して通っていただける医院を目指します。</p>
    <div class="dir-photo img" role="img" aria-label="院長の写真" style="background:linear-gradient(135deg,#d4dce4,#9fb0c0)"></div>
    <div class="btn-more" style="top:370px">詳しくはこちら ›</div>
  </div>
</section>

<section class="info">
  <div class="col" style="left:130px">
    <h2>お知らせ</h2>
    <ul class="news">
      <li><time class="en">2018.05.01</time>5月の休診日についてお知らせいたします。</li>
      <li><time class="en">2018.04.20</time>ネット予約の受付を開始しました。</li>
      <li><time class="en">2018.04.10</time>ゴールデンウィーク中の診療について。</li>
      <li><time class="en">2018.04.01</time>すずらん耳鼻咽喉科を開院しました。</li>
      <li><time class="en">2018.03.25</time>内覧会のご案内を掲載しました。</li>
    </ul>
    <div class="btn-more" style="top:330px">一覧はこちら ›</div>
  </div>
  <div class="divider"></div>
  <div class="col" style="left:640px">
    <h2>ブログ</h2>
    <div class="blog-item"><div class="img" role="img" aria-label="ブログ記事の写真" style="background:#cfdfe4"></div>
      <div><span class="tag">ブログ</span> <span class="en" style="font-size:10px;color:var(--muted)">2018.05.01</span><p>花粉症の季節の過ごし方</p><small>鼻の症状を和らげるための日常の工夫をご紹介します。</small></div></div>
    <div class="blog-item"><div class="img" role="img" aria-label="ブログ記事の写真" style="background:#e4cfb7"></div>
      <div><span class="tag">ブログ</span> <span class="en" style="font-size:10px;color:var(--muted)">2018.04.20</span><p>漢方治療のよくあるご質問</p><small>初めての方からいただく質問にお答えします。</small></div></div>
    <div class="btn-more" style="top:330px">一覧はこちら ›</div>
  </div>
</section>

<section class="map" role="img" aria-label="医院周辺の地図">
  <svg class="abs" style="left:578px;top:110px" width="44" height="56" viewBox="0 0 44 56"><path d="M22 54C8 34 2 26 2 20a20 20 0 0 1 40 0c0 6-6 14-20 34z" fill="#8fb83a"/><circle cx="22" cy="20" r="7" fill="#fff"/></svg>
</section>

<footer class="footer">
  <div class="to-top"><svg width="14" height="10" viewBox="0 0 14 10"><path d="M1 8l6-6 6 6" fill="none" stroke="#fff" stroke-width="2"/></svg></div>
  <div class="abs" style="left:150px;top:50px">
    <div class="f-logo"><i></i>すずらん耳鼻咽喉科</div>
    <div class="en" style="font-size:10px;letter-spacing:2px;margin:4px 0 14px 24px">SUZURAN ENT CLINIC</div>
    <div style="font-size:11px">〒310-0099 茨城県水戸市みどり町1-2-3</div>
    <div class="tel"><small>tel.</small>029-555-0184</div>
    <span class="btn-reserve" style="background:var(--green)">ネット予約はこちらから ›</span>
    <table class="hours" style="margin-top:14px">
      <tr><th>診療時間</th><th>月</th><th>火</th><th>水</th><th>木</th><th>金</th><th>土</th><th>日</th></tr>
      <tr><td>9:00 - 12:30</td><td class="o">●</td><td class="o">●</td><td class="o">●</td><td>／</td><td class="o">●</td><td class="o">●</td><td>／</td></tr>
      <tr><td>15:00 - 18:30</td><td class="o">●</td><td class="o">●</td><td class="o">●</td><td>／</td><td class="o">●</td><td>／</td><td>／</td></tr>
    </table>
  </div>
  <div class="f-nav" style="left:600px"><span>HOME</span><span>初めての方へ</span><span>医院について</span><span>当院の特徴</span><span>院長紹介</span><span>よくある質問</span></div>
  <div class="f-nav" style="left:730px"><h4>耳鼻咽喉科</h4><span>耳の病気</span><span>鼻の病気</span><span>口・のどの病気</span><span>頭・顔・首の病気</span><span>風邪の症状</span></div>
  <div class="f-nav" style="left:880px"><h4>漢方治療</h4><span>更年期の症状にお悩みの方へ</span><span>冷えにお悩みの方へ</span><span>不眠にお悩みの方へ</span><span>めまい・耳鳴りにお悩みの方へ</span><span>体質改善</span></div>
  <div class="copy en">© SUZURAN ENT CLINIC</div>
</footer>

</body>
</html>
```